Modern, Playful Illustrated Book Cover for Women’s Wellness / Self-Help Book

Project Scope
This contest is for the front cover only of a 6x9 nonfiction book. This contest is for the front cover only. The spine and back cover will be completed at a later stage once final production specifications are available.

Title:
Breathe! Here Comes My Turn Again

Subtitle:
Thirty Garden Lessons with Quiet Stories About Patience, Seasonal Rhythms, and the Art of Waiting Well

Author:
Lorena Whitcombe, M.Ed.

I want a modern, playful, bold, polished illustrated cover that feels like a contemporary women’s wellness/self-help book — not a traditional diet book.

The cover should especially resonate with Black women, while still feeling welcoming to a broader female audience.

Illustration only — no photography and no real people.

If hands or other human elements are included, they should be fully illustrated as Black women using rich brown skin tones in a modern, sophisticated way.

Please do not use black silhouettes, shadow figures, faceless silhouette-style people, or generic darkened human shapes. I want the representation to feel intentional, contemporary, and fully illustrated.

I am open to creative interpretations around themes such as:

everyday choices
habits
cravings and temptation
changing patterns
letting go
taking back control
progress
reclaiming your life

The title should be the visual star and should remain easy to read at thumbnail size.

Please avoid:

bathroom scales as the main image
measuring tape
before-and-after bodies
body silhouettes
generic fitness imagery
salads or smoothies as the main concept
medical or clinical imagery
childish cartoons
generic stock-vector or template-looking designs

I want the overall feel to be fresh, modern, warm, confident, playful, sophisticated, and visually engaging.

Originality
Please create an original concept specifically for this book. Do not recreate or closely imitate an existing published book cover.

Target Market(s)

Adult women, especially Black women, who want a practical, encouraging, realistic approach to weight loss, healthier habits, and sustainable change. Must haves

Industry/Entity Type

Publishing / Books / Wellness / Self-Help

Requirements
Must have
• Modern illustrated cover; strong, highly readable title; polished contemporary wellness/self-help feel; illustration only, no photography; if human elements are used, they should reflect Black women with rich brown skin tones; front cover only.
Nice to have
• Creative visual ideas around everyday choices, habits, cravings, letting go, progress, and taking back control. Open to illustrated hands, food-related interactions, everyday objects, or symbolic imagery if used in a sophisticated way. Colors: Open to designer color recommendations; I prefer a fresh, modern, warm, energetic, sophisticated palette.
Should not have
• No black silhouettes or shadow figures; no real people or photography; no scales as the main image; no measuring tape, before/after bodies, body silhouettes, generic fitness imagery, salads/smoothies as the main concept, medical imagery, childish cartoons, or generic template/stock-vector-looking designs.

```html
<!DOCTYPE html>
<html lang="en">
<head>
<meta charset="utf-8">
<title>Breathe! Here Comes My Turn Again — Front Cover</title>
<link rel="stylesheet" href="https://fonts.googleapis.com/css2?family=Archivo:wght@400;500;700;800&family=DM+Serif+Display&family=Outfit:wght@300&display=swap">
<style>
  :root {
    --stage: #e8e5e0;
    --cover-cream: #fff8f0;
    --cover-white: #fffdfb;
    --cover-peach: #fde3d2;
    --cover-blush: #fbc6b8;
    --title-green: #46ad5c;
    --title-lime: #cdd63e;
    --ink-olive: #4a3c12;
    --ink-soft: #3f3527;
    --art-petal: #f2c9bb;
    --art-leaf: #a9b894;
    --art-skin: #b98a6c;
    --art-cloth: #f1e4d9;
  }
  * { margin: 0; padding: 0; box-sizing: border-box; }
  html, body {
    width: 1200px; height: 803px; overflow: hidden;
    background: var(--stage);
  }
  .cover {
    position: absolute;
    left: 347px; top: 21px;
    width: 506px; height: 760px;
    overflow: hidden;
    background:
      radial-gradient(ellipse 60% 22% at 50% 100%, var(--cover-blush) 0%, rgba(251,198,184,0) 100%),
      radial-gradient(ellipse 55% 35% at 10% 8%, var(--cover-peach) 0%, rgba(253,227,210,0) 100%),
      radial-gradient(ellipse 50% 40% at 95% 90%, #fdebd6 0%, rgba(253,235,214,0) 100%),
      linear-gradient(180deg, #fde9de 0%, var(--cover-white) 35%, var(--cover-cream) 70%, #fde6d8 100%);
    box-shadow: 0 6px 18px rgba(0,0,0,0.12);
  }
  .cover-art {
    position: absolute;
    left: 196px; top: 56px;
    width: 264px; height: 280px;
    border-radius: 28px;
    background: linear-gradient(165deg,
      var(--art-petal) 0%,
      var(--art-leaf) 38%,
      var(--art-skin) 68%,
      var(--art-cloth) 100%);
  }
  .title-main {
    position: absolute;
    left: 70px; top: 530px;
    transform-origin: top left;
    transform: rotate(-90deg);
    font-family: "DM Serif Display", serif;
    font-size: 100px;
    line-height: 1;
    white-space: nowrap;
    background: linear-gradient(90deg, var(--title-green) 0%, #8cc24a 55%, var(--title-lime) 100%);
    -webkit-background-clip: text;
    background-clip: text;
    color: transparent;
  }
  .title-rest {
    position: absolute;
    left: 224px; top: 346px;
    font-family: "Archivo", sans-serif;
    color: var(--ink-olive);
    letter-spacing: -0.5px;
  }
  .title-rest .line { display: block; }
  .title-rest .light { font-size: 30px; font-weight: 500; line-height: 36px; }
  .title-rest .heavy { font-size: 48px; font-weight: 800; line-height: 52px; letter-spacing: -1px; }
  .subtitle {
    position: absolute;
    left: 58px; top: 596px;
    width: 390px;
    text-align: center;
    text-wrap: balance;
    font-family: "Outfit", sans-serif;
    font-weight: 300;
    font-size: 14px;
    line-height: 20px;
    color: var(--ink-soft);
  }
  .author {
    position: absolute;
    left: 0; top: 676px;
    width: 100%;
    text-align: center;
    font-family: "Archivo", sans-serif;
    color: var(--ink-soft);
  }
  .author-name { display: block; font-size: 19px; font-weight: 700; letter-spacing: -0.2px; }
  .author-credential { display: block; font-size: 12px; font-weight: 700; margin-top: 3px; }
</style>
</head>
<body>
  <main class="cover">
    <div class="cover-art" role="img" aria-label="Illustration of a Black woman in a seated yoga side stretch among pink blossoms and green leaves"></div>
    <h1 class="title">
      <span class="title-main">Breathe!</span>
      <span class="title-rest">
        <span class="line light">Here</span>
        <span class="line light">Comes My</span>
        <span class="line heavy">Turn</span>
        <span class="line heavy">Again.</span>
      </span>
    </h1>
    <p class="subtitle">Thirty Garden Lessons with Quiet Stories About Patience, Seasonal Rhythms, and the Art of Waiting&nbsp;Well</p>
    <p class="author">
      <span class="author-name">LORENA WHITCOMBE</span>
      <span class="author-credential">M.Ed.</span>
    </p>
  </main>
</body>
</html>
```